Establishing a website for a non profit organisation

The foundation is called:

German: Edle Betagte Vereinigung des Hauses Lindmark e.V.

Englisch (Translation): Noble venerable Union of House Lindmark e.V.

The foundation is a legal nonprofit organization with the purpose to help people in need. The foundation - a charitable organization - donates funds and supports solely and directly people living in Frankfurt and in Germany.

In some cases the foundation works together with other charitable organizations that support projects to help people in need.

The foundation also functions as trustee with powers of administration of property in trust with a legal obligation to administer it solely for the purposes specified. The purpose is not to generate/obtain wealth for shareholders but to respectfully execute the benevolent intentions of the founders/testators in the interest of the legatee.

The foundation was established in 1408.

The website should give a good and easy overview about the foundation work.
It should be easy to figure out how to participate and help the organisation.
Either you can participate with a one time donation, with a regular donation or with a testament.

For those with donation it is possible to hand over an contribution receipt for tax purposes.

The main color should be red: RGB R:229 - G:47 - B:34

```html
<!DOCTYPE html>
<html lang="en">
<head>
<meta charset="utf-8">
<title>Edle Betagte Vereinigung des Hauses Lindmark e.V.</title>
<link href="https://fonts.googleapis.com/css2?family=Lato:wght@400;700&family=Roboto:wght@400&display=swap" rel="stylesheet">
<style>
:root{
  --red:#e52f22;
  --blue:#1b5d7b;
  --teal:#1f5b78;
  --page:#e9e9e9;
  --white:#ffffff;
  --text:#555555;
  --muted:#9a9a9a;
  --link:#4a86e8;
  --rule:#dddddd;
}
*{margin:0;padding:0;box-sizing:border-box}
html,body{width:1200px;height:900px;overflow:hidden}
body{background:var(--page);font-family:'Lato',sans-serif;position:relative}
.top-nav{position:absolute;left:82px;top:22px;display:flex;align-items:center;font-family:'Roboto',sans-serif;font-size:17px;color:#666}
.top-nav a{color:#666;text-decoration:none}
.top-nav .sep{color:var(--red);margin:0 10px}
.site-title{position:absolute;left:122px;top:66px;font-size:30px;font-weight:700;color:var(--red);white-space:nowrap}
.btn-donate{position:absolute;left:967px;top:26px;width:200px;height:38px;background:var(--red);color:var(--white);font-size:18px;font-weight:700;display:flex;align-items:center;justify-content:center}
.search{position:absolute;left:975px;top:79px;width:192px;height:28px;background:var(--white);border-radius:4px;font-size:15px;font-style:italic;color:#aaa;padding:5px 9px}
.band-edge{position:absolute;top:128px;height:35px;background:var(--red)}
.tab{position:absolute;top:128px;height:35px;width:258px;display:flex;align-items:center;justify-content:center;gap:8px;color:var(--white);font-weight:700;font-size:19px;background:var(--blue)}
.tab.active{background:var(--red)}
.tab svg{width:18px;height:18px}
.hero{position:absolute;left:38px;top:163px;width:1129px;height:353px;background:linear-gradient(100deg,#7b7f93 0%,#d9c9bd 25%,#c98f6c 45%,#e2d6cb 65%,#8b98ad 100%)}
.hero-caption{position:absolute;left:781px;top:62px;width:306px;height:183px;background:rgba(31,91,125,.8);color:var(--white);padding:18px 24px}
.hero-caption h2{font-size:31px;font-weight:400;line-height:36px}
.hero-caption p{font-size:15px;line-height:18px;margin-top:0}
.hero-cta{position:absolute;left:781px;top:257px;width:306px;height:58px;background:var(--red);color:var(--white);text-align:center;padding-top:9px}
.hero-cta strong{display:block;font-size:19px}
.hero-cta span{display:block;font-size:11px;font-weight:700;margin-top:2px}
.dots{position:absolute;right:8px;bottom:8px;display:flex;gap:4px}
.dots i{width:12px;height:12px;border-radius:50%;background:var(--white)}
.dots i.on{background:var(--red);border:2px solid var(--white)}
.panel{position:absolute;top:529px;height:371px;background:var(--white)}
.main{left:38px;width:764px}
.side{left:815px;width:352px}
.panel h3{position:absolute;color:var(--red);font-weight:700}
.main h3{left:44px;top:16px;font-size:24px}
.side h3{left:27px;top:12px;font-size:22px}
.rule{position:absolute;height:1px;background:var(--rule)}
.article{position:absolute;left:44px;width:522px}
.article h4{font-size:18px;font-weight:700;color:#666;margin-bottom:10px}
.article p{font-size:15.5px;line-height:20px;color:var(--muted)}
.article a{display:block;margin-top:10px;font-size:16px;font-weight:700;color:var(--link);text-decoration:none}
.thumb{position:absolute;left:602px;width:118px;height:117px}
.news-item{position:absolute;left:27px;width:300px}
.news-item h5{font-size:16px;font-weight:700;color:var(--teal);margin-bottom:3px}
.news-item p{font-size:16px;line-height:20px;color:var(--muted)}
</style>
</head>
<body>
<nav class="top-nav">
  <a>Home</a><span class="sep">|</span><a>History</a><span class="sep">|</span><a>What We Do</a><span class="sep">|</span><a>Possibilities</a><span class="sep">|</span><a>Participate</a><span class="sep">|</span><a>Donation</a><span class="sep">|</span><a>News</a><span class="sep">|</span><a>Contact</a>
</nav>
<h1 class="site-title">Edle Betagte Vereinigung des Hauses Lindmark e.V.</h1>
<div class="btn-donate">DONATE</div>
<div class="search">search</div>

<div class="band-edge" style="left:0;width:73px"></div>
<div class="band-edge" style="left:1131px;width:69px"></div>
<div class="tab active" style="left:79px">
  <svg viewBox="0 0 20 20"><path d="M10 1 3 4v6c0 4 3 7.5 7 9 4-1.5 7-5 7-9V4z" fill="#fff"/><text x="10" y="14" font-size="11" font-weight="700" text-anchor="middle" fill="#e52f22" font-family="Lato,sans-serif">?</text></svg>WHAT WE DO</div>
<div class="tab" style="left:341px">
  <svg viewBox="0 0 20 20"><path d="M10 2 3 10h4.5v8h5v-8H17z" fill="#fff"/></svg>POSSIBILITIES</div>
<div class="tab" style="left:604px">
  <svg viewBox="0 0 20 20"><path d="M10 17 3 10a4 4 0 0 1 7-5 4 4 0 0 1 7 5z" fill="none" stroke="#fff" stroke-width="2"/></svg>PARTICIPATE</div>
<div class="tab" style="left:866px">
  <svg viewBox="0 0 20 20"><path d="M10 18 2.5 10a4.5 4.5 0 0 1 7.5-5.5A4.5 4.5 0 0 1 17.5 10z" fill="none" stroke="#fff" stroke-width="2"/><text x="10" y="13.5" font-size="9" font-weight="700" text-anchor="middle" fill="#fff" font-family="Lato,sans-serif">$</text></svg>DONATE</div>

<section class="hero" role="img" aria-label="Photo of two hands clasped in a helping handshake against a cloudy sky">
  <div class="hero-caption">
    <h2>LOREM IPSUM DOLOR SIT AMET</h2>
    <p>CONSECTETUR ADIPISICING ELIT, SED DO EIUSMOD TEMPOR INCIDI-DUNT UT LABORE ET DOLORE MAGNA.</p>
  </div>
  <div class="hero-cta"><strong>MAKE A DONATION TODAY</strong><span>ONE TIME / LIFE TIME OPTIONS</span></div>
  <div class="dots"><i class="on"></i><i></i><i></i><i></i></div>
</section>

<main class="panel main">
  <h3>Look What We Do</h3>
  <div class="rule" style="left:44px;top:58px;width:675px"></div>
  <article class="article" style="top:83px">
    <h4>Lorem ipsum dolor sit amet constra de amor</h4>
    <p>Proin gravida nibh vel velit auctor aliquet. Aenean sollicitudin, lorem quis bibendum auctor, Duis sed odio sit amet nibh vulputate cursus a sit amet mauris. Morbi accumsan ipsum velit. Nam nec tellus a odio tincidunt<br>auctor a ornare odio.</p>
    <a>Read more...</a>
  </article>
  <div class="thumb" style="top:90px;background:linear-gradient(135deg,#7fc6c0,#c8a48f 55%,#8a6b58)" role="img" aria-label="Photo of a caring hand holding an elderly person's hands"></div>
  <div class="rule" style="left:44px;top:259px;width:675px"></div>
  <article class="article" style="top:294px">
    <h4>Ed do eiusmod tempor incididunt ut labore et dolore</h4>
    <p>Proin gravida nibh vel velit auctor aliquet. Aenean sollicitudin, lorem quis bibendum auctor, Duis sed odio sit amet nibh vulputate cursus a sit amet mauris.</p>
  </article>
  <div class="thumb" style="top:302px;background:linear-gradient(180deg,#a8cde6,#b7a58c 45%,#a4584c)" role="img" aria-label="Photo of a large group of people on a historic stone wall"></div>
</main>

<aside class="panel side">
  <h3>Latest News</h3>
  <div class="rule" style="left:27px;top:47px;width:295px"></div>
  <div class="news-item" style="top:54px"><h5>Amet constra de amor</h5><p>This is Draftwork's version&nbsp; of Lorem Ipsum. Proin gravida nibh vel velit ....</p></div>
  <div class="rule" style="left:27px;top:131px;width:302px"></div>
  <div class="news-item" style="top:142px"><h5>Lorem ipsum dolor sit</h5><p>This is Draftwork's version&nbsp; of Lorem Ipsum. Proin gravida nibh vel velit ....</p></div>
  <div class="rule" style="left:27px;top:219px;width:302px"></div>
  <div class="news-item" style="top:233px"><h5>Ucididunt ut labore et dolore magna</h5><p>This is Draftwork's version&nbsp; of Lorem Ipsum. Proin gravida nibh vel velit ....</p></div>
  <div class="rule" style="left:27px;top:313px;width:302px"></div>
  <div class="news-item" style="top:331px"><h5>Adipisicing elit, sed do eiusmod tem</h5><p>This is Draftwork's version&nbsp; of Lorem Ipsum.</p></div>
</aside>
</body>
</html>
```